PLM - Business Card Design Project

We need a business card based on our logo
Updates

Hi I just upload logo file in AI format Thanks and regards

Target Market(s)

Bank, Big companies, Business owners

Industry/Entity Type

Business

Font styles to use
Sans Serif

```html
<!DOCTYPE html>
<html lang="en">
<head>
<meta charset="utf-8">
<title>PLM – Business Card</title>
<link href="https://fonts.googleapis.com/css2?family=Questrial&display=swap" rel="stylesheet">
<style>
  :root {
    --navy: #132a4e;
    --slate: #7f9392;
    --grey-text: #8a9594;
    --card: #ffffff;
    --backdrop: #4b4b4b;
  }
  * { margin: 0; padding: 0; box-sizing: border-box; }
  html, body {
    width: 1200px; height: 1000px; overflow: hidden;
    background: var(--backdrop);
    font-family: "Questrial", "Century Gothic", sans-serif;
  }
  .card {
    position: absolute;
    background: var(--card);
    box-shadow: 0 6px 18px rgba(0,0,0,.35);
    overflow: hidden;
  }
  .card--front { left: 185px; top: 119px; width: 640px; height: 375px; }
  .card--back  { left: 335px; top: 515px; width: 643px; height: 375px; }

  .brand { position: absolute; text-align: center; color: var(--navy); }
  .brand__mark { display: block; font-weight: 400; line-height: 1; letter-spacing: 2px; }
  .brand__name { display: block; white-space: nowrap; }
  .brand__tagline { display: block; color: var(--grey-text); white-space: nowrap; }

  .card--front .brand { left: 0; right: 0; top: 88px; }
  .card--front .brand__mark { font-size: 168px; height: 140px; }
  .card--front .brand__name { font-size: 22px; margin-top: 2px; }
  .card--front .brand__tagline { font-size: 12px; margin-top: 3px; }

  .card--back .brand { left: 355px; width: 250px; top: 190px; }
  .card--back .brand__mark { font-size: 126px; height: 106px; }
  .card--back .brand__name { font-size: 17px; }
  .card--back .brand__tagline { font-size: 9px; margin-top: 2px; }

  .person { position: absolute; left: 25px; top: 56px; }
  .person__name { font-size: 22px; color: var(--navy); letter-spacing: .5px; }
  .person__role { font-size: 15px; color: var(--grey-text); margin-top: 2px; }

  .contacts { position: absolute; left: 27px; top: 166px; list-style: none; }
  .contacts li {
    display: flex; align-items: center; height: 22.5px;
    font-size: 15px; color: var(--navy);
  }
  .contacts svg { width: 17px; height: 17px; margin-right: 12px; fill: var(--navy); }

  .office { position: absolute; left: 27px; top: 268px; font-size: 15px; line-height: 22.5px; }
  .office__name { color: var(--navy); font-weight: 700; letter-spacing: .2px; }
  .office__line { color: var(--grey-text); letter-spacing: .5px; }

  .band { position: absolute; left: 0; bottom: 0; width: 643px; height: 18px; }
</style>
</head>
<body>

<section class="card card--front">
  <div class="brand">
    <span class="brand__mark">PLM</span>
    <span class="brand__name">Cabinet Perrin &amp; Lemaire</span>
    <span class="brand__tagline">Expertise-comptable • Audit • Conseil</span>
  </div>
</section>

<section class="card card--back">
  <div class="person">
    <p class="person__name">JULIEN MARCHAND</p>
    <p class="person__role">Director</p>
  </div>

  <ul class="contacts">
    <li>
      <svg viewBox="0 0 16 16" aria-hidden="true"><path d="M4 0h8a1.5 1.5 0 0 1 1.5 1.5v13A1.5 1.5 0 0 1 12 16H4a1.5 1.5 0 0 1-1.5-1.5v-13A1.5 1.5 0 0 1 4 0zm.2 2v10.5h7.6V2zM8 13.3a.9.9 0 1 0 0 1.8.9.9 0 0 0 0-1.8z"/></svg>
      555 204 6718
    </li>
    <li>
      <svg viewBox="0 0 16 16" aria-hidden="true"><path d="M0 3h16v10H0zm1.6 1.2L8 9l6.4-4.8zM1.2 5v7l4.4-3.7zm13.6 0-4.4 3.3 4.4 3.7zM6.6 9.1l-4.5 3.7h11.8L9.4 9.1 8 10.2z"/></svg>
      yourname@plm.com
    </li>
    <li>
      <svg viewBox="0 0 16 16" aria-hidden="true"><path d="M8 0a8 8 0 1 0 0 16A8 8 0 0 0 8 0zm-1 2.2c-.6.9-1.8 1.1-2.2 2.2-.3.9.8 1.4 1.6 1.3.9 0 1.3.9.9 1.6-.5.9-1.7 1-1.8 2.2 0 1 .9 1.6.8 2.7-.1.8-.7 1.3-1 1.6A6.5 6.5 0 0 1 7 2.2zm3.2.3a6.5 6.5 0 0 1 3.9 7.1c-.6-.5-1.5-.4-2-1.1-.5-.8.2-1.9-.6-2.6-.7-.6-1.9.1-2.3-.8-.3-.9.9-1.4 1-2.3z"/></svg>
      www.plm.com
    </li>
  </ul>

  <div class="office">
    <p class="office__name">CABINET PERRIN &amp; LEMAIRE</p>
    <p class="office__line">P.O.Box 48, Springfield,</p>
    <p class="office__line">US 65801</p>
  </div>

  <div class="brand">
    <span class="brand__mark">PLM</span>
    <span class="brand__name">Cabinet Perrin &amp; Lemaire</span>
    <span class="brand__tagline">Expertise-comptable • Audit • Conseil</span>
  </div>

  <svg class="band" viewBox="0 0 643 18" preserveAspectRatio="none" aria-hidden="true">
    <polygon points="0,0 355,0 347,18 0,18" fill="var(--navy)"/>
    <polygon points="362,0 643,0 643,18 354,18" fill="var(--slate)"/>
  </svg>
</section>

</body>
</html>
```